Now Leasing Banner

Looking for a banner that says the following information approx 4' x 30'

Now Leasing Maplewood Terrace 925-318-6054

Target Market(s)

Drive by traffic

Industry/Entity Type

Residential property management

Requirements
Must have
• Clear and readable from a distance

```html
<!DOCTYPE html>
<html lang="en">
<head>
<meta charset="utf-8">
<title>Now Leasing Banner</title>
<link rel="stylesheet" href="https://fonts.googleapis.com/css2?family=Lexend:wght@500&display=swap">
<style>
  :root {
    --headline: #fff200;
    --frame: #ffffff;
    --sky-top: #6f8aa8;
    --sky-mid: #9fb0bf;
    --town: #5b6448;
    --town-deep: #3f4a33;
    --hill: #6f8a3d;
  }
  html, body {
    margin: 0;
    padding: 0;
    width: 1200px;
    height: 240px;
    overflow: hidden;
  }
  .banner {
    position: relative;
    width: 1200px;
    height: 240px;
    overflow: hidden;
    font-family: "Lexend", sans-serif;
  }
  .banner__scenery {
    position: absolute;
    inset: 0;
    background:
      radial-gradient(ellipse 40% 30% at 55% 95%, rgba(111,138,61,.55), transparent 70%),
      radial-gradient(ellipse 30% 25% at 12% 90%, rgba(111,138,61,.6), transparent 70%),
      linear-gradient(180deg, var(--sky-top) 0%, var(--sky-mid) 30%, #7d8a86 40%, var(--town) 55%, var(--town-deep) 80%, var(--hill) 100%);
  }
  .banner__scenery::after {
    content: "";
    position: absolute;
    inset: 0;
    background: rgba(0,0,0,.12);
  }
  .banner__photo {
    position: absolute;
  }
  .banner__photo--exterior {
    left: 16px;
    top: 19px;
    width: 206px;
    height: 206px;
  }
  .banner__photo--interior {
    left: 968px;
    top: 14px;
    width: 212px;
    height: 212px;
  }
  .banner__message {
    position: absolute;
    left: 240px;
    right: 240px;
    top: 62px;
    text-align: center;
    color: var(--headline);
    line-height: 1;
  }
  .banner__headline {
    margin: 0;
    font-size: 50px;
    font-weight: 500;
    letter-spacing: 0.5px;
  }
  .banner__phone {
    margin: 26px 0 0;
    display: inline-flex;
    align-items: center;
    gap: 14px;
    font-size: 50px;
    font-weight: 500;
    color: var(--headline);
    text-decoration: none;
    letter-spacing: 1px;
  }
  .banner__phone svg {
    width: 50px;
    height: 50px;
  }
</style>
</head>
<body>
  <div class="banner">
    <div class="banner__scenery" role="img" aria-label="Aerial view of a hillside suburb with homes, trees and green hills under a blue sky"></div>

    <svg class="banner__photo banner__photo--exterior" viewBox="0 0 206 206" role="img" aria-label="Two-storey apartment building with tiled roof and exterior stairs">
      <defs>
        <linearGradient id="exteriorTone" x1="0" y1="0" x2="0" y2="1">
          <stop offset="0" stop-color="#3a78c9"/>
          <stop offset="0.3" stop-color="#d9c9ad"/>
          <stop offset="0.75" stop-color="#c9b79a"/>
          <stop offset="1" stop-color="#5f7a3a"/>
        </linearGradient>
      </defs>
      <polygon points="103,4 180,41 199,124 146,192 60,192 7,124 26,41" fill="url(#exteriorTone)" stroke="var(--frame)" stroke-width="5" stroke-linejoin="round"/>
    </svg>

    <svg class="banner__photo banner__photo--interior" viewBox="0 0 212 212" role="img" aria-label="Bright living room with sofa, cushions, fireplace and arched window">
      <defs>
        <linearGradient id="interiorTone" x1="0" y1="0" x2="1" y2="1">
          <stop offset="0" stop-color="#e6ddd3"/>
          <stop offset="0.55" stop-color="#d8d2cb"/>
          <stop offset="1" stop-color="#8a7a6a"/>
        </linearGradient>
      </defs>
      <polygon points="106,4 185,42 205,128 150,198 62,198 7,128 27,42" fill="url(#interiorTone)" stroke="var(--frame)" stroke-width="5" stroke-linejoin="round"/>
    </svg>

    <div class="banner__message">
      <h1 class="banner__headline">Now Leasing Maplewood Terrace</h1>
      <a class="banner__phone" href="tel:9253186054">
        <svg viewBox="0 0 24 24" fill="none" stroke="currentColor" stroke-width="1.4" stroke-linecap="round" stroke-linejoin="round" aria-hidden="true">
          <path d="M5 3.5h3l1.5 4-2 1.3a11 11 0 0 0 7.7 7.7l1.3-2 4 1.5v3a2 2 0 0 1-2.2 2A17 17 0 0 1 3 5.7 2 2 0 0 1 5 3.5z"/>
          <path d="M14.5 6.5a4 4 0 0 1 3 3"/>
          <path d="M14.5 3a7.5 7.5 0 0 1 6.5 6.5"/>
        </svg>
        <span>925-318-6054</span>
      </a>
    </div>
  </div>
</body>
</html>
```